Business Card Design

Attached is the logo of the store.

Information needed on the business card:

www.vault82vino.com
info@vault82vino.com
412 7th Ave NY, NY 10036
Tel:(646) 555-0147

Store Hours
Mon-Sat Noon-10pm
Sun Noon-8pm

Free Deliveries

Industry/Entity Type

Business

Contact Information for Business Card

Bramble 82 Wine & Spirits

```html
<!DOCTYPE html>
<html lang="en">
<head>
<meta charset="utf-8">
<title>Bramble 82 Wine &amp; Spirits — Business Card</title>
<link href="https://fonts.googleapis.com/css2?family=Questrial&display=swap" rel="stylesheet">
<style>
  :root {
    --backdrop: #5e5e5e;
    --ink-dark: #1b1a1a;
    --ink-grey: #4a4a4a;
    --paper: #f7f6f3;
    --accent-red: #e0193a;
    --white: #ffffff;
    --card-shadow: rgba(0, 0, 0, 0.35);
  }
  * { margin: 0; padding: 0; box-sizing: border-box; }
  html, body { width: 1200px; height: 875px; overflow: hidden; }
  body {
    background: var(--backdrop);
    font-family: "Questrial", "Century Gothic", sans-serif;
    position: relative;
  }

  .brand-mark {
    position: absolute;
    left: 44px;
    top: 40px;
    color: var(--white);
    line-height: 1;
  }
  .brand-mark__name { font-size: 78px; letter-spacing: 1px; display: block; }
  .brand-mark__tag { font-size: 32px; letter-spacing: 2px; display: block; margin-top: 10px; }

  .card {
    position: absolute;
    width: 580px;
    height: 331px;
    box-shadow: 0 14px 30px var(--card-shadow);
    overflow: hidden;
  }

  /* Front card */
  .card--front {
    left: 570px;
    top: 70px;
    background: var(--ink-dark);
  }
  .card--front .card__logo {
    position: absolute;
    left: 0; right: 0;
    top: 70px;
    text-align: center;
    color: var(--white);
    line-height: 1;
  }
  .card--front .card__logo-name { font-size: 52px; display: block; }
  .card--front .card__logo-tag { font-size: 20px; letter-spacing: 1px; display: block; margin-top: 8px; }
  .card--front .card__band {
    position: absolute;
    left: 0; right: 0; bottom: 0;
    height: 92px;
    background: var(--accent-red);
    color: var(--white);
    font-size: 34px;
    letter-spacing: 4px;
    display: flex;
    align-items: center;
    justify-content: center;
  }

  /* Back card */
  .card--back {
    left: 90px;
    top: 455px;
    background: var(--paper);
    color: var(--ink-grey);
  }
  .card--back .card__logo {
    position: absolute;
    left: 34px;
    top: 30px;
    line-height: 1;
  }
  .card--back .card__logo-name { font-size: 38px; display: block; }
  .card--back .card__logo-tag { font-size: 15px; letter-spacing: 1px; display: block; margin-top: 5px; }
  .store-hours {
    position: absolute;
    right: 30px;
    top: 34px;
    text-align: right;
    font-size: 22px;
    line-height: 1.15;
  }
  .store-hours__title { font-weight: 700; color: var(--ink-dark); font-family: "Questrial", sans-serif; }
  .card--back .card__band {
    position: absolute;
    left: 0; right: 0;
    top: 132px;
    height: 50px;
    background: var(--accent-red);
    color: var(--white);
    font-size: 27px;
    letter-spacing: 4px;
    display: flex;
    align-items: center;
    justify-content: center;
  }
  .contact-list {
    position: absolute;
    left: 0; right: 0;
    top: 196px;
    list-style: none;
    text-align: center;
    font-size: 25px;
    line-height: 1.1;
    color: var(--ink-grey);
  }
</style>
</head>
<body>
  <div class="brand-mark">
    <span class="brand-mark__name">Bramble 82</span>
    <span class="brand-mark__tag">wine &amp; spirits</span>
  </div>

  <section class="card card--front" aria-label="Business card front">
    <div class="card__logo">
      <span class="card__logo-name">Bramble 82</span>
      <span class="card__logo-tag">wine &amp; spirits</span>
    </div>
    <div class="card__band">www.vault82vino.com</div>
  </section>

  <section class="card card--back" aria-label="Business card back">
    <div class="card__logo">
      <span class="card__logo-name">Bramble 82</span>
      <span class="card__logo-tag">wine &amp; spirits</span>
    </div>
    <div class="store-hours">
      <div class="store-hours__title">Store Hours</div>
      <div>Mon-Sat Noon-10pm</div>
      <div>Sun Noon-8pm</div>
    </div>
    <div class="card__band">FREE DELIVERIES</div>
    <ul class="contact-list">
      <li>www.vault82vino.com</li>
      <li>info@vault82vino.com</li>
      <li>412 7th Ave | NY, NY 10036</li>
      <li>Tel:(646) 555-0147</li>
    </ul>
  </section>
</body>
</html>
```